Business Card Design Project

We require a professional business card designed for our consulting organisation that has the same theme and colours as our logo except for the grey.

Colours on the front should predominately be white however some reference to our logo colours except for the grey.

The back of the card should be have background colour that aligns with our logo colour.

Layout, style and design is up to the designer. So send through your designs

Details are attached in the word document project brief.

Target Market(s)

Target market are large corporate organisations

Industry/Entity Type

Business

Requirements
Must have
• Content on the front must have:

Dean Halvorsen
Managing Director

P: 0417 285 394
E: Dean@brevolinkpartners.com
W: www.brevolinkpartners.com

Content on the back must have the words:
Alliances
Placement
Training
Support

Design Colours
Must align to our logo

```html
<!DOCTYPE html>
<html lang="en">
<head>
<meta charset="utf-8">
<title>BrevoLink Partners – Business Cards</title>
<link rel="stylesheet" href="https://fonts.googleapis.com/css2?family=Open+Sans:wght@400;600;700&display=swap">
<style>
  :root {
    --brand-blue: #1f7fc9;
    --brand-blue-dark: #13609f;
    --brand-blue-light: #5aa9e3;
    --brand-blue-pale: #cfe6f8;
    --text-dark: #3d3e40;
    --card-white: #ffffff;
    --backdrop: #e9e7e3;
    --divider: #c9c9c9;
    --divider-on-blue: rgba(255,255,255,0.6);
  }
  * { margin: 0; padding: 0; box-sizing: border-box; }
  html, body {
    width: 1200px; height: 720px; overflow: hidden;
    background: var(--backdrop);
    font-family: "Open Sans", Arial, sans-serif;
    color: var(--text-dark);
  }
  .canvas { position: relative; width: 1200px; height: 720px; }

  .card {
    position: absolute; top: 205px;
    width: 540px; height: 310px;
    background: var(--card-white);
    box-shadow: 0 6px 18px rgba(0,0,0,0.18);
    overflow: hidden;
  }
  .card--front { left: 40px; }
  .card--back  { left: 620px; background: var(--brand-blue); color: var(--card-white); }

  .brand {
    position: absolute; display: flex; align-items: center; gap: 12px;
    color: var(--brand-blue); font-weight: 700; white-space: nowrap;
  }
  .brand__dot { border-radius: 50%; background: var(--brand-blue); flex: none; }

  /* Front */
  .card--front .brand { left: 120px; top: 48px; font-size: 32px; }
  .card--front .brand__dot { width: 30px; height: 30px; }

  .person { position: absolute; left: 44px; top: 168px; }
  .person__name { color: var(--brand-blue); font-weight: 700; font-size: 19px; }
  .person__role { font-size: 15px; color: var(--text-dark); margin-top: 2px; }

  .contact-divider {
    position: absolute; left: 222px; top: 128px; width: 1px; height: 92px;
    background: var(--divider);
  }
  .contact-list { position: absolute; left: 236px; top: 130px; list-style: none; }
  .contact-list li {
    display: flex; align-items: center; gap: 8px;
    font-size: 13px; line-height: 28px; color: var(--text-dark);
  }
  .contact-list svg { width: 16px; height: 16px; flex: none; }

  .front-bands { position: absolute; left: 0; bottom: 0; width: 540px; height: 80px; }

  /* Back */
  .card--back .brand { left: 70px; top: 70px; font-size: 38px; color: var(--card-white); }
  .card--back .brand__dot { width: 38px; height: 38px; background: var(--card-white); }

  .services {
    position: absolute; left: 150px; top: 160px;
    display: flex; align-items: stretch; font-size: 22px; line-height: 28px; color: var(--card-white);
  }
  .services__col { padding: 0 16px; }
  .services__col:first-child { padding-left: 0; }
  .services__rule { width: 1px; background: var(--divider-on-blue); }

  .back-url {
    position: absolute; left: 0; right: 0; top: 262px; text-align: center;
    font-size: 16px; letter-spacing: 1px; color: var(--card-white);
  }
  .back-url__accent { color: var(--brand-blue-pale); }
</style>
</head>
<body>
<main class="canvas">

  <section class="card card--front" aria-label="Business card front">
    <div class="brand">
      <span class="brand__dot"></span>
      <span class="brand__name">BrevoLink Partners</span>
    </div>

    <div class="person">
      <p class="person__name">Dean Halvorsen</p>
      <p class="person__role">Managing Director</p>
    </div>

    <div class="contact-divider"></div>
    <ul class="contact-list">
      <li>
        <svg viewBox="0 0 16 16" aria-hidden="true"><circle cx="8" cy="8" r="7.5" fill="none" stroke="var(--brand-blue)"/><path d="M5.5 4.5l1.6-.3.8 2-1 .8a5 5 0 0 0 2.1 2.1l.8-1 2 .8-.3 1.6c-3.5.3-6.3-2.5-6-6z" fill="var(--brand-blue)"/></svg>
        <span>0417 285 394</span>
      </li>
      <li>
        <svg viewBox="0 0 16 16" aria-hidden="true"><circle cx="8" cy="8" r="7.5" fill="var(--brand-blue)"/><rect x="4" y="5.5" width="8" height="5.5" fill="#fff"/><path d="M4 5.5l4 3 4-3" fill="none" stroke="var(--brand-blue)" stroke-width="0.9"/></svg>
        <span>Dean@brevolinkpartners.com</span>
      </li>
      <li>
        <svg viewBox="0 0 16 16" aria-hidden="true"><circle cx="8" cy="8" r="7.5" fill="var(--brand-blue)"/><circle cx="8" cy="8" r="4.2" fill="none" stroke="#fff" stroke-width="0.9"/><ellipse cx="8" cy="8" rx="1.8" ry="4.2" fill="none" stroke="#fff" stroke-width="0.9"/><path d="M3.8 8h8.4" stroke="#fff" stroke-width="0.9"/></svg>
        <span>www.brevolinkpartners.com</span>
      </li>
    </ul>

    <svg class="front-bands" viewBox="0 0 540 80" preserveAspectRatio="none" aria-hidden="true">
      <polygon points="0,66 230,60 250,80 0,80" fill="var(--brand-blue-dark)"/>
      <polygon points="250,80 230,60 540,8 540,80" fill="var(--brand-blue-light)"/>
      <polygon points="250,80 236,66 540,22 540,80" fill="var(--brand-blue)"/>
    </svg>
  </section>

  <section class="card card--back" aria-label="Business card back">
    <div class="brand">
      <span class="brand__dot"></span>
      <span class="brand__name">BrevoLink Partners</span>
    </div>

    <div class="services">
      <div class="services__col"><p>Alliances</p><p>Placement</p></div>
      <div class="services__rule"></div>
      <div class="services__col"><p>Training</p><p>Support</p></div>
    </div>

    <p class="back-url">www.<span class="back-url__accent">brevolink</span>partners.com</p>
  </section>

</main>
</body>
</html>
```